New emergency medical service needs a marketing flyer for prospective customers

We need a tri fold brochure on an 8.5 X 11 stock for a new emergency medical service in Pennsylvania. We provide basic first aid and now Covid-19 pre screening and temperature monitoring for special events, large gatherings and businesses. Examples of these would be but not limited to: Sporting events, carnivals, festivals, craft shows, warehouses, churches, manufacturing facilities, industrial buildings, large construction sites, multi occupancy officer buildings. The market for this is pretty much untouched and endless. we would like to use gray as the back ground color and obviously our logo. The final design should grab their attention and communicate the importance of having trained and certified professionals at their event or facility. We want to give them that piece of mind they are in good hands with us.

Target Market(s)

primary focus is going to be on businesses with large offices, large buildings or lots of foot traffic in and out of the building

Requirements
Must have
• gray background, pictures, company phone # , company web site, and contact email address. I will provide all that information to the winner to add at the end.
Nice to have
• pictures that covers the whole front cover with logo at top

```html
<!DOCTYPE html>
<html lang="en">
<head>
<meta charset="utf-8">
<title>Ridgeline Medical – Tri-fold Brochure</title>
<link href="https://fonts.googleapis.com/css2?family=Exo+2:wght@700&family=Open+Sans:wght@400;600&display=swap" rel="stylesheet">
<style>
:root{
  --navy:#2c3a96;
  --teal:#10b6a1;
  --bg:#d5d5d8;
  --white:#ffffff;
  --text:#4a4a4a;
}
*{margin:0;padding:0;box-sizing:border-box}
html,body{width:1200px;height:2566px;overflow:hidden;background:var(--bg);font-family:"Open Sans",Arial,sans-serif;color:var(--text)}
.canvas{position:relative;width:1200px;height:2566px}
.sheet,.panel{position:absolute;box-shadow:6px 6px 10px rgba(0,0,0,.22);overflow:hidden}
.sheet .panel{box-shadow:none}
.abs{position:absolute}
.fill-navy{background:var(--navy)}
.fill-teal{background:var(--teal)}
.fill-white{background:var(--white)}
.heading{font-family:"Exo 2",sans-serif;font-weight:700;text-transform:uppercase;color:var(--navy);font-size:19px;line-height:23px}
.title{font-family:"Exo 2",sans-serif;font-weight:700;font-size:20px;color:var(--white)}
.body{font-size:12.4px;line-height:15.1px;text-align:justify;text-align-last:left}
.body.white{color:var(--white)}
.photo{position:absolute}
.photo.festival{background:linear-gradient(135deg,#6f7c4a,#b79aa8 45%,#3b3f45)}
.photo.field{background:linear-gradient(160deg,#cfcabc,#8a7d66 55%,#b3472f 60%,#7d8f52 75%,#8d8571)}
.photo.doctor{background:linear-gradient(120deg,#dfe9f3,#f5f8fb 40%,#8fb3d6 75%,#3c70a8)}
.photo.factory{background:linear-gradient(135deg,#5b6675,#b98a5a 45%,#9a2a1e 70%,#c8c9cc)}
.photo.control{background:linear-gradient(135deg,#d9dde2,#2b4a8a 50%,#7b8896)}
.photo.scan{background:linear-gradient(135deg,#2f2a28,#d8c8bb 45%,#c9d0d9 70%,#4a3a2e)}
.photo.thermal{background:linear-gradient(135deg,#e9eceb,#9aa8a3 50%,#2f3e5a)}
.photo.crew{background:linear-gradient(135deg,#27302a,#7fb3d1 45%,#2e5a3a 75%,#1a1a1a)}
.photo.ppe{background:linear-gradient(135deg,#5aa3d8,#9fd1ef 50%,#b8433a 80%,#d9c24a)}
.map{position:absolute;border-radius:50%;border:6px solid var(--teal);background:radial-gradient(circle,#f4efe6,#e2ddd2 70%,#cfd8e6)}
.brand{font-family:"Exo 2",sans-serif;font-weight:700;color:var(--navy);display:flex;align-items:center;gap:10px;white-space:nowrap}
.brand .dot{border-radius:50%;background:var(--teal);flex:none}
.brand.light{color:var(--white)}
.brand.cover{left:0;right:0;top:0;height:168px;justify-content:center;gap:14px;font-size:40px;line-height:42px}
.url-bar{position:absolute;left:0;right:0;bottom:0;height:50px;display:flex;align-items:center;justify-content:center;color:var(--white);font-size:20px}
.contact{position:absolute;right:25px;text-align:right;color:var(--white);font-size:12.4px;line-height:15px}
.contact h3{font-family:"Exo 2",sans-serif;font-weight:700;font-size:19px;margin-bottom:8px}
.contact .rule{display:block;width:26px;height:2px;background:var(--white);margin:6px 0 6px auto}
.contact .rule.wide{width:100px}
.steps{list-style:none}
.steps li{display:flex;align-items:center;height:60px;color:var(--white)}
.steps .num{font-family:"Exo 2",sans-serif;font-weight:700;font-size:48px;width:52px;text-align:left}
.steps p{font-size:12.4px;line-height:15px;text-align:justify;width:236px}
.industries{list-style:disc;padding-left:20px;color:var(--white);font-size:12.4px;line-height:15.1px}
.badge{position:absolute;border-radius:50%;background:#4a63b8;border:4px solid #1e2a70}
</style>
</head>
<body>
<div class="canvas">

  <section class="sheet" style="left:70px;top:47px;width:1073px;height:761px">
    <div class="panel fill-white" style="left:0;top:0;width:353px;height:761px">
      <div class="photo festival" role="img" aria-label="First aid tent and ambulance at an outdoor festival" style="left:0;top:0;width:353px;height:198px"></div>
      <h2 class="heading abs" style="left:32px;top:221px">Festival Medical Services</h2>
      <p class="body abs" style="left:32px;top:256px;width:292px">Lorem assen Sie sich fiihren.Lorem ipsum dolor sit amet, consectetuer adipiscing elit, sed diam nonummy nibh euismod tincidunt ut laoreet dolore magna aliquam erat volutpat. Ut wisi enim ad minim veniam, quis nostrud exerci tation ullamcorper suscipit lobortis nisl ut aliquip ex ea</p>
      <h2 class="heading abs" style="left:32px;top:370px">Manufacturing Facilities<br>Medical Services</h2>
      <div class="photo factory" role="img" aria-label="Collage of factory floors, welding and production lines" style="left:33px;top:429px;width:288px;height:208px"></div>
      <p class="body abs" style="left:32px;top:647px;width:292px">Lorem assen Sie sich fiihren.Lorem ipsum dolor sit amet, consectetuer adipiscing elit, sed diam nonummy nibh euismod tincidunt ut laoreet dolore magna aliquam erat volutpat. Ut wisi enim ad minim veniam, quis nostrud exerci tation ullamcorper suscipit lobortis nisl ut aliquip ex ea</p>
    </div>

    <div class="panel" style="left:353px;top:0;width:360px;height:761px">
      <div class="abs fill-teal" style="left:0;top:0;width:360px;height:240px">
        <h2 class="title abs" style="left:26px;top:40px">Lorem Ipsum Dolor</h2>
        <p class="body white abs" style="left:26px;top:70px;width:313px">Lorem ipsum dolor sit amet, consectetuer adipiscing elit, sed diam nonummy nibh euismod tincidunt ut laoreet dolore magna aliquam Lorem ipsum dolor sit amet, consectetuer adipiscing elit, sed diam nonummy nibh euismod tincidunt ut laoreet dolore magna aliquam erat volutpat. Ut wisi enim ad minim veniam, quis nostrud exerci tation ullamcorper suscipit lobortis nisl ut aliquip ex ea commodo consequat. Duis autem vel eum iriure dolor in hendrerit in vulputate</p>
      </div>
      <div class="photo field" role="img" aria-label="Medics treating a player on a sports field" style="left:0;top:240px;width:360px;height:240px"></div>
      <div class="abs fill-navy" style="left:0;top:480px;width:360px;height:281px">
        <div class="map" role="img" aria-label="Street map showing the office location" style="left:10px;top:48px;width:188px;height:188px"></div>
        <div class="brand light abs" style="right:25px;top:30px;font-size:18px"><span class="dot" style="width:14px;height:14px;background:var(--white)"></span>Ridgeline Medical</div>
        <div class="contact" style="top:92px">
          <h3>Contact Us</h3>
          <span class="rule wide"></span>
          Alder Street 48<br>17011 Camp Hill
          <span class="rule"></span>
          +1 (717) 555 0142<br>+1 (717) 555 0143<br>info@ridgelinemedical.com
          <span class="rule"></span>
          www.ridgelinemedical.com
        </div>
      </div>
    </div>

    <div class="panel fill-white" style="left:713px;top:0;width:360px;height:761px">
      <div class="brand cover abs"><span class="dot" style="width:36px;height:36px"></span><span>Ridgeline<br>Medical</span></div>
      <div class="photo doctor" role="img" aria-label="Doctor in white coat with stethoscope holding a tablet" style="left:0;top:168px;width:360px;height:543px"></div>
      <div class="url-bar fill-navy">www.ridgelinemedical.com</div>
    </div>
  </section>

  <section class="sheet" style="left:70px;top:878px;width:1072px;height:762px">
    <div class="panel" style="left:0;top:0;width:352px;height:762px">
      <div class="abs fill-navy" style="left:0;top:0;width:352px;height:254px">
        <h2 class="heading abs" style="left:36px;top:33px;color:var(--white)">About</h2>
        <div class="brand light abs" style="left:36px;top:64px;font-size:24px;line-height:26px"><span class="dot" style="width:18px;height:18px;background:var(--white)"></span><span>Ridgeline<br>Medical</span></div>
        <div class="badge" aria-hidden="true" style="left:232px;top:26px;width:94px;height:94px"></div>
        <p class="body white abs" style="left:36px;top:140px;width:291px">Lorem assen Sie sich fiihren.Lorem ipsum dolor sit amet, consectetuer adipiscing elit, sed diam nonummy nibh euismod tincidunt ut laoreet dolore magna aliquam erat volutpat. Ut wisi enim ad minim veniam, quis nostrud exerci tation ullamcorper suscipit lobortis nisl ut aliquip ex ea</p>
      </div>
      <div class="photo control" role="img" aria-label="Staff in masks at a control room monitoring desk" style="left:0;top:254px;width:352px;height:235px"></div>
      <div class="abs fill-navy" style="left:0;top:489px;width:352px;height:223px">
        <ol class="steps abs" style="left:40px;top:22px">
          <li><span class="num">1</span><p>Lorem assen Sie sich fiihren.Lorem ipsum dolor sit amet, consectetuer adipiscing elit, sed diam.</p></li>
          <li><span class="num">2</span><p>Lorem assen Sie sich fiihren.Lorem ipsum dolor sit amet, consectetuer adipiscing elit, sed diam.</p></li>
          <li><span class="num">3</span><p>Lorem assen Sie sich fiihren.Lorem ipsum dolor sit amet, consectetuer adipiscing elit, sed diam.</p></li>
        </ol>
      </div>
      <div class="url-bar fill-teal">www.ridgelinemedical.com</div>
    </div>

    <div class="panel fill-white" style="left:352px;top:0;width:360px;height:762px">
      <h2 class="heading abs" style="left:26px;top:29px">Covid-19 Pre Screening and<br>Temperature Monitoring</h2>
      <div class="photo scan" role="img" aria-label="Masked woman having her temperature taken with an infrared thermometer" style="left:0;top:93px;width:360px;height:239px"></div>
      <p class="body abs" style="left:36px;top:347px;width:291px">Lorem assen Sie sich fiihren.Lorem ipsum dolor sit amet, consectetuer adipiscing elit, sed diam nonummy nibh euismod tincidunt ut laoreet dolore magna aliquam erat volutpat. Ut wisi enim ad minim veniam, quis nostrud exerci tation ullamcorper suscipit lobortis nisl ut aliquip ex ea</p>
      <div class="photo thermal" role="img" aria-label="Thermal camera screening people at a building entrance" style="left:0;top:452px;width:360px;height:180px"></div>
      <p class="body abs" style="left:36px;top:646px;width:291px">Lorem assen Sie sich fiihren.Lorem ipsum dolor sit amet, consectetuer adipiscing elit, sed diam nonummy nibh euismod tincidunt ut laoreet dolore magna aliquam erat volutpat. Ut wisi enim ad minim veniam, quis nostrud exerci tation ullamcorper suscipit lobortis nisl ut aliquip ex ea</p>
    </div>

    <div class="panel fill-teal" style="left:712px;top:0;width:360px;height:762px">
      <h2 class="heading abs" style="left:35px;top:33px;color:var(--white)">Industries We Are Working</h2>
      <p class="body white abs" style="left:35px;top:75px;width:289px">We provide basic first aid and now Covid-19 pre screening and temperature monitoring for special events, large gatherings and businesses.</p>
      <p class="body white abs" style="left:35px;top:136px;width:289px">Examples of these would be but not limited to:</p>
      <ul class="industries abs" style="left:36px;top:166px">
        <li>Sporting Events,</li><li>Carnivals,</li><li>Festivals,</li><li>Craft Shows,</li><li>Warehouses,</li><li>Churches,</li><li>Manufacturing Facilities,</li><li>Industrial Buildings,</li><li>Large Construction Sites,</li><li>Multi Occupancy Officer Buildings</li>
      </ul>
      <div class="photo crew" role="img" aria-label="Medical crew in hair caps screening a visitor" style="left:0;top:334px;width:360px;height:201px"></div>
      <div class="photo ppe" role="img" aria-label="Workers in protective suits checking temperatures in a crowd" style="left:0;top:542px;width:360px;height:205px"></div>
    </div>
  </section>

  <section class="panel fill-white" style="left:252px;top:1737px;width:360px;height:761px">
    <div class="brand cover abs"><span class="dot" style="width:36px;height:36px"></span><span>Ridgeline<br>Medical</span></div>
    <div class="photo doctor" role="img" aria-label="Doctor in white coat with stethoscope holding a tablet" style="left:0;top:168px;width:360px;height:543px"></div>
    <div class="url-bar fill-navy">www.ridgelinemedical.com</div>
  </section>

  <section class="panel" style="left:675px;top:1737px;width:360px;height:761px">
    <div class="abs fill-teal" style="left:0;top:0;width:360px;height:240px">
      <h2 class="title abs" style="left:26px;top:40px">Lorem Ipsum Dolor</h2>
      <p class="body white abs" style="left:26px;top:70px;width:313px">Lorem ipsum dolor sit amet, consectetuer adipiscing elit, sed diam nonummy nibh euismod tincidunt ut laoreet dolore magna aliquam Lorem ipsum dolor sit amet, consectetuer adipiscing elit, sed diam nonummy nibh euismod tincidunt ut laoreet dolore magna aliquam erat volutpat. Ut wisi enim ad minim veniam, quis nostrud exerci tation ullamcorper suscipit lobortis nisl ut aliquip ex ea commodo consequat. Duis autem vel eum iriure dolor in hendrerit in vulputate</p>
    </div>
    <div class="photo field" role="img" aria-label="Medics treating a player on a sports field" style="left:0;top:240px;width:360px;height:240px"></div>
    <div class="abs fill-navy" style="left:0;top:480px;width:360px;height:281px">
      <div class="map" role="img" aria-label="Street map showing the office location" style="left:10px;top:48px;width:188px;height:188px"></div>
      <div class="brand light abs" style="right:25px;top:30px;font-size:18px"><span class="dot" style="width:14px;height:14px;background:var(--white)"></span>Ridgeline Medical</div>
      <div class="contact" style="top:92px">
        <h3>Contact Us</h3>
        <span class="rule wide"></span>
        Alder Street 48<br>17011 Camp Hill
        <span class="rule"></span>
        +1 (717) 555 0142<br>+1 (717) 555 0143<br>info@ridgelinemedical.com
        <span class="rule"></span>
        www.ridgelinemedical.com
      </div>
    </div>
  </section>

</div>
</body>
</html>
```